RT Consult - Web Design Upgrade

We have recently designed a website (http://www.rtconsult-demo.com.au) which requires more creative and professional inputs. The website was designed using 'jolly portals site builder template' and it is currently available for viewing on the internet. Also, you are able to access the PDF files for the 6 main pages (i.e. Home, About, Services, Contaminated Land Management, Groundwater Management and Contact).

The current website has 17 pages, however, your design may only be required for the 6 main pages.

Currently the website background is white but we are open to other colours provided the company logo is adjusted accordingly.

The idea is to upgrade the existing design and, if possible, continue using 'jolly portals' as the preferred web host. So we are not sure if the design should be coded or uncoded...we leave it to your proficiency and advice.

Target Market(s)

Government organisations, landowners and developers, waste and utilities companies, community organisations and individuals.

Industry/Entity Type

Internet

Number of Pages Required

5+ page

Font styles to use
Sans Serif

Colors
0355a3
3176b5
9ccb3b
acd037
ffffff

Requirements
Nice to have
• Sliding images

```html
<!DOCTYPE html>
<html lang="en">
<head>
<meta charset="utf-8">
<title>RT Consult – Home</title>
<link href="https://fonts.googleapis.com/css2?family=Open+Sans:wght@400;600&family=Roboto:wght@400;500&display=swap" rel="stylesheet">
<style>
  :root {
    --blue: #0355a3;
    --blue-mid: #3176b5;
    --blue-dark: #024a8f;
    --green: #9ccb3b;
    --green-alt: #acd037;
    --green-deep: #6fa21d;
    --white: #ffffff;
    --charcoal: #272b33;
    --text-grey: #555a61;
    --ink: #3a3e44;
    --muted: #b5bac1;
    --border: #c9c9c9;
  }
  * { box-sizing: border-box; margin: 0; padding: 0; }
  html, body { width: 1092px; height: 1200px; overflow: hidden; background: var(--white); }
  body { position: relative; font-family: "Open Sans", sans-serif; color: var(--text-grey); }

  .site-header { position: absolute; left: 0; top: 0; width: 1092px; height: 150px; background: var(--white); }
  .brand { position: absolute; left: 168px; top: 58px; }
  .brand-name { font-family: "Open Sans", sans-serif; font-weight: 400; font-size: 26px; color: var(--ink); white-space: nowrap; }

  .call-us { position: absolute; left: 594px; top: 36px; font-size: 14px; color: #555; white-space: nowrap; }
  .call-us strong { font-weight: 400; font-size: 19px; color: var(--blue); margin-left: 2px; }
  .social { position: absolute; left: 793px; top: 33px; display: flex; gap: 3px; list-style: none; }
  .social li { width: 25px; height: 25px; border-radius: 50%; border: 2px solid #d7d7d7; background: var(--blue-mid); }
  .social li:nth-child(2) { background: #3aa9e0; }
  .social li:nth-child(3) { background: #d5483b; }
  .social li:nth-child(4) { background: #c42b1d; }
  .social li:nth-child(5) { background: #ef6a1c; }

  .search { position: absolute; left: 715px; top: 82px; width: 213px; height: 44px; border: 1px solid var(--border); background: var(--white); }
  .search span { position: absolute; left: 17px; top: 14px; font-size: 11px; color: #888; }
  .search svg { position: absolute; right: 16px; top: 14px; }

  .main-nav { position: absolute; left: 0; top: 150px; width: 1092px; height: 52px; background: linear-gradient(var(--blue-mid) 0, var(--blue) 45%, var(--blue-dark) 100%); border-top: 2px solid var(--blue-mid); }
  .main-nav ul { list-style: none; }
  .main-nav li { position: absolute; top: 20px; font-size: 11.5px; color: var(--white); white-space: nowrap; }
  .main-nav li.is-active { left: 165px; top: -6px; width: 68px; height: 63px; background: var(--green); text-align: center; padding-top: 26px; }

  .hero { position: absolute; left: 0; top: 202px; width: 1092px; height: 523px;
    background: linear-gradient(160deg, #5f7248 0%, #3f5532 30%, #7c7f7a 55%, #565a4d 80%, #45583a 100%); }
  .hero-caption { position: absolute; left: 165px; top: 281px; width: 464px; height: 86px; background: rgba(255,255,255,0.72); }
  .hero-caption h1 { position: absolute; left: 25px; top: 22px; font-family: "Open Sans", sans-serif; font-weight: 400; font-size: 29px; color: #2b2b2b; white-space: nowrap; }
  .hero-arrow { position: absolute; top: 246px; }
  .hero-arrow.prev { left: 20px; }
  .hero-arrow.next { left: 1044px; }

  .features { position: absolute; left: 0; top: 725px; width: 1092px; height: 232px; background: var(--charcoal); }
  .feature { position: absolute; top: 0; width: 370px; text-align: center; }
  .feature.land { left: 170px; }
  .feature.water { left: 552px; }
  .feature-icon { position: absolute; left: 125px; top: -75px; width: 120px; height: 120px; border-radius: 50%;
    background: radial-gradient(circle at 50% 35%, var(--green-alt), var(--green-deep)); border: 2px solid #8cbf2a; }
  .feature-icon svg { position: absolute; left: 30px; top: 30px; }
  .feature h2 { position: absolute; left: 0; top: 50px; width: 370px; font-family: "Roboto", sans-serif; font-weight: 400; font-size: 19px; color: var(--white); }
  .feature p { position: absolute; left: 0; top: 79px; width: 370px; font-size: 10.2px; line-height: 22px; color: var(--muted); }
  .btn { position: absolute; left: 136px; top: 171px; width: 100px; height: 35px; border: 1px solid #2a78c4; border-radius: 2px;
    background: linear-gradient(var(--blue-mid), var(--blue)); color: var(--white); font-size: 10.5px; line-height: 33px; text-align: center; }

  .intro { position: absolute; left: 0; top: 957px; width: 1092px; height: 179px; text-align: center; }
  .intro h2 { position: absolute; left: 0; top: 31px; width: 1092px; font-family: "Roboto", sans-serif; font-weight: 400; font-size: 24px; color: var(--blue); }
  .intro p { position: absolute; left: 160px; top: 70px; width: 772px; font-size: 10.1px; line-height: 23.5px; color: var(--text-grey); }

  .site-footer { position: absolute; left: 0; top: 1136px; width: 1092px; height: 64px; background: var(--blue); border-top: 2px solid var(--blue-mid); color: var(--white); font-size: 10.5px; }
  .footer-links { position: absolute; left: 163px; top: 24px; }
  .footer-links span + span { margin-left: 8px; }
  .copyright { position: absolute; right: 164px; top: 24px; }
</style>
</head>
<body>
  <header class="site-header">
    <div class="brand">
      <div class="brand-name">RT Consult</div>
    </div>
    <div class="call-us">Call Us : <strong>61 400 555 019</strong></div>
    <ul class="social" aria-label="Social links">
      <li></li><li></li><li></li><li></li><li></li>
    </ul>
    <div class="search">
      <span>Search...</span>
      <svg width="16" height="16" viewBox="0 0 16 16"><circle cx="6.5" cy="6.5" r="5" fill="none" stroke="#aaa" stroke-width="1.6"/><line x1="10.2" y1="10.2" x2="14.5" y2="14.5" stroke="#aaa" stroke-width="1.8"/></svg>
    </div>
  </header>

  <nav class="main-nav">
    <ul>
      <li class="is-active">HOME</li>
      <li style="left:253px">ABOUT</li>
      <li style="left:330px">SERVICES</li>
      <li style="left:419px">CONTAMINATED LAND MANAGEMENT</li>
      <li style="left:654px">GROUNDWATER MANAGEMENT</li>
      <li style="left:856px">CONTACT</li>
    </ul>
  </nav>

  <section class="hero" role="img" aria-label="Aerial photograph of a suburban development site with trees, car parks and a building under construction">
    <div class="hero-caption"><h1>Environmental Site Assessment</h1></div>
    <svg class="hero-arrow prev" width="26" height="36" viewBox="0 0 26 36"><polyline points="20,4 6,18 20,32" fill="none" stroke="rgba(255,255,255,0.75)" stroke-width="5"/></svg>
    <svg class="hero-arrow next" width="26" height="36" viewBox="0 0 26 36"><polyline points="6,4 20,18 6,32" fill="none" stroke="rgba(255,255,255,0.75)" stroke-width="5"/></svg>
  </section>

  <section class="features">
    <article class="feature land">
      <div class="feature-icon">
        <svg width="60" height="60" viewBox="0 0 60 60">
          <path d="M30 34 V20" stroke="#fff" stroke-width="3"/>
          <path d="M30 22 C22 22 17 16 17 10 C24 10 30 15 30 22 Z" fill="#fff"/>
          <path d="M30 22 C38 22 43 16 43 10 C36 10 30 15 30 22 Z" fill="#fff"/>
          <path d="M6 44 C16 34 26 34 34 38 L44 38 C48 38 48 43 44 43 L32 43 L48 36 C52 35 54 39 51 41 L36 50 C28 54 16 52 6 50 Z" fill="#fff"/>
        </svg>
      </div>
      <h2>Contaminated Land Management</h2>
      <p>Ut wisi enim ad minim veniam, quis nostrud exerci tation ullamcorper suscipit lobortis nisl ut aliquip ex ea commodo consequat. Duis autem vel eum iriure dolor in hendrerit in vulputate velit esse molestie consequat, vel illum dolore eu feugiat nulla facilisis at vero eros et accumsan.</p>
      <div class="btn">READ MORE</div>
    </article>
    <article class="feature water">
      <div class="feature-icon">
        <svg width="60" height="60" viewBox="0 0 60 60">
          <rect x="24" y="8" width="12" height="5" fill="#fff"/>
          <rect x="28" y="12" width="4" height="8" fill="#fff"/>
          <rect x="20" y="19" width="36" height="12" rx="2" fill="#fff"/>
          <path d="M6 22 H22 V30 H14 V40 H6 Z" fill="#fff"/>
          <path d="M10 44 C7 48 7 51 10 51 C13 51 13 48 10 44 Z" fill="#fff"/>
        </svg>
      </div>
      <h2>Groundwater Management</h2>
      <p>Ut wisi enim ad minim veniam, quis nostrud exerci tation ullamcorper suscipit lobortis nisl ut aliquip ex ea commodo consequat. Duis autem vel eum iriure dolor in hendrerit in vulputate velit esse molestie consequat, vel illum dolore eu feugiat nulla facilisis at vero eros et accumsan.</p>
      <div class="btn">READ MORE</div>
    </article>
  </section>

  <section class="intro">
    <h2>Working to Sustain our Environments</h2>
    <p>Lorem ipsum dolor sit amet, consectetuer adipiscing elit, sed diam nonummy nibh euismod tincidunt ut laoreet dolore magna aliquam erat volutpat. Ut wisi enim ad minim veniam, quis nostrud exerci tation ullamcorper suscipit lobortis nisl ut aliquip ex ea commodo consequat. Duis autem vel eum iriure dolor in hendrerit in vulputate velit esse molestie consequat, vel illum dolore eu feugiat nulla facilisis at vero eros et accumsan et iusto odio dignissim qui blandit praesent luptatum zzril delenit augue duis dolore te feugait nulla facilisi.</p>
  </section>

  <footer class="site-footer">
    <div class="footer-links"><span>Privacy Policy</span><span>Sitemap</span></div>
    <div class="copyright">Copyrights@ 2014 Rock &amp; Terrain Consulting Pty Ltd. All Right Reserved.</div>
  </footer>
</body>
</html>
```